Business Card Design Project

See the detainl of the Fernlo company project I also have live: http://tasks.plomwerk.com/task.aspx?id=384920

Reason: I am waiting to select a logo design and ideally the business card design will be from the same person

```html
<!DOCTYPE html>
<html lang="en">
<head>
<meta charset="utf-8">
<title>Halvern LLP – Business Card</title>
<link rel="stylesheet" href="https://fonts.googleapis.com/css2?family=Lato:wght@400;700;900&display=swap">
<style>
  :root {
    --brand-blue: #1ba3d6;
    --ink: #151515;
    --band-text: #d3dde2;
    --card-white: #ffffff;
    --card-grey: #e6e6e6;
    --rule-black: #0d0d0d;
    --backdrop: #2a2a2a;
  }
  * { margin: 0; padding: 0; box-sizing: border-box; }
  html, body { width: 1200px; height: 900px; overflow: hidden; }
  body {
    background: var(--backdrop);
    font-family: "Lato", Arial, sans-serif;
    position: relative;
  }
  .business-card {
    position: absolute;
    left: 180px; top: 210px;
    width: 840px; height: 480px;
    border-radius: 26px;
    overflow: hidden;
    background: linear-gradient(160deg, var(--card-white) 0%, var(--card-white) 45%, var(--card-grey) 100%);
  }
  .card-band { position: absolute; left: 0; top: 0; width: 840px; height: 480px; }
  .company-name {
    position: absolute; top: 62px; left: 0; width: 100%;
    text-align: center;
    color: var(--brand-blue);
    font-weight: 900; font-size: 46px; letter-spacing: 1px;
  }
  .divider {
    position: absolute; left: 417px; top: 150px;
    width: 6px; height: 182px; background: var(--brand-blue);
  }
  .person {
    position: absolute; right: 445px; top: 150px; text-align: right; color: var(--ink);
  }
  .person-name { color: var(--brand-blue); font-weight: 900; font-size: 31px; line-height: 36px; }
  .person-role { font-weight: 700; font-size: 20px; line-height: 24px; }
  .company-web { margin-top: 30px; font-weight: 700; font-size: 21px; line-height: 28px; }
  .company-web .accent, .partnership .accent { color: var(--brand-blue); font-weight: 400; }
  .partnership { font-weight: 700; font-size: 21px; line-height: 28px; }
  .partnership .accent { font-size: 23px; }
  .contact-list { position: absolute; left: 445px; top: 150px; list-style: none; }
  .contact-item {
    display: flex; align-items: center; gap: 12px;
    height: 35px; font-size: 21px; font-weight: 700; color: var(--ink);
  }
  .contact-icon { width: 26px; height: 26px; flex: none; }
  .tag {
    position: absolute; background: var(--brand-blue); color: var(--card-white);
    font-weight: 700; font-size: 21px; letter-spacing: 0.5px;
    padding: 2px 10px; line-height: 28px;
  }
  .tag-innovation { left: 452px; top: 298px; }
  .tag-registered { left: 80px; top: 362px; }
  .address { position: absolute; color: var(--band-text); font-weight: 700; font-size: 21px; line-height: 27px; }
  .address-innovation { left: 455px; top: 352px; }
  .address-registered { right: 445px; top: 412px; text-align: right; }
</style>
</head>
<body>
  <div class="business-card">
    <svg class="card-band" viewBox="0 0 840 480" aria-hidden="true">
      <path d="M0 402 H420 V338 H840 V346 H428 V410 H0 Z" fill="var(--rule-black)"/>
      <path d="M0 410 H428 V346 H840 V480 H0 Z" fill="var(--brand-blue)"/>
    </svg>

    <h1 class="company-name">HALVERN LLP</h1>

    <div class="person">
      <p class="person-name">YOUR NAME</p>
      <p class="person-role">Centre Director</p>
      <p class="company-web">www.<span class="accent">halvern</span>.co.uk</p>
      <p class="partnership">Partnership No. <span class="accent">OC482716</span></p>
    </div>

    <div class="divider"></div>

    <ul class="contact-list">
      <li class="contact-item">
        <svg class="contact-icon" viewBox="0 0 26 26" aria-label="Telephone"><circle cx="13" cy="13" r="13" fill="var(--brand-blue)"/><path d="M6 10 Q13 5 20 10 L18 12 L16 11 L16 9 Q13 8 10 9 L10 11 L8 12 Z" fill="#fff"/><rect x="8" y="13" width="10" height="6" rx="1" fill="#fff"/></svg>
        <span>+44 (0)1632 960081</span>
      </li>
      <li class="contact-item">
        <svg class="contact-icon" viewBox="0 0 26 26" aria-label="Mobile"><circle cx="13" cy="13" r="13" fill="var(--brand-blue)"/><rect x="8.5" y="5.5" width="9" height="15" rx="1.5" fill="none" stroke="#fff" stroke-width="2"/></svg>
        <span>+44 (0)7700 900XXX</span>
      </li>
      <li class="contact-item">
        <svg class="contact-icon" viewBox="0 0 26 26" aria-label="Fax"><circle cx="13" cy="13" r="13" fill="var(--brand-blue)"/><rect x="9" y="6" width="8" height="5" fill="#fff"/><rect x="6" y="11" width="14" height="7" rx="1" fill="#fff"/><rect x="9" y="16" width="8" height="4" fill="#fff" stroke="var(--brand-blue)" stroke-width="1"/></svg>
        <span>(0)1632 960082</span>
      </li>
      <li class="contact-item">
        <svg class="contact-icon" viewBox="0 0 26 26" aria-label="Email"><circle cx="13" cy="13" r="13" fill="var(--brand-blue)"/><rect x="6" y="8" width="14" height="10" fill="#fff"/><path d="M6 8 L13 14 L20 8" fill="none" stroke="var(--brand-blue)" stroke-width="1.5"/></svg>
        <span>tom.ashby@halvern.co.uk</span>
      </li>
    </ul>

    <p class="tag tag-innovation">INNOVATION CENTRE</p>
    <p class="address address-innovation">41 Norbridge Science Park<br>Elmway Road, Norbridge, NB4 1QA</p>

    <p class="tag tag-registered">REGISTERED OFFICE:</p>
    <p class="address address-registered">Birch Lodge, 7B Harrow Rd,<br>Norbridge, NB5 2KT</p>
  </div>
</body>
</html>
```